Breezeway Climate Business Card Design

Design new, 2 sides, business cards for a residential and light commercial heating, air conditioning contractor.

Target Market(s)

Homeowners, small businesses

Industry/Entity Type

Business

Contact Information for Business Card

Dominic Vasquerelli
Phone - 555-214-6837
Email
Address - PO box 618
Millbrook NJ 07999
Website - www.BreezewayClimateLLC.example

Requirements
Must have
• logo, company colors, standard size with no die cut, so I can use printhaven

```html
<!DOCTYPE html>
<html lang="en">
<head>
<meta charset="utf-8">
<title>Breezeway Climate Business Cards</title>
<link rel="stylesheet" href="https://fonts.googleapis.com/css2?family=Roboto:wght@400;700&display=swap">
<style>
  :root {
    --backdrop: #e4e4e8;
    --brand-red: #9e2233;
    --brand-orange: #f28a30;
    --card-white: #ffffff;
    --ink: #1c1c1c;
    --cream: #fbe7b0;
  }
  * { box-sizing: border-box; margin: 0; padding: 0; }
  html, body {
    width: 1200px; height: 800px; overflow: hidden;
    background: var(--backdrop);
    font-family: "Roboto", Arial, sans-serif;
  }
  .card-sheet {
    position: relative; width: 1200px; height: 800px;
    display: flex; align-items: center; justify-content: center; gap: 60px;
  }
  .card {
    position: relative; width: 525px; height: 300px; overflow: hidden;
    box-shadow: 0 6px 18px rgba(0,0,0,0.18);
  }

  /* Back side: contact details */
  .card--back { background: var(--brand-orange); }
  .card--back .contact-panel {
    position: absolute; left: 26px; right: 26px; top: 30px; bottom: 30px;
    background: var(--card-white);
    border: 6px solid var(--brand-red);
    display: flex; flex-direction: column; align-items: center;
    padding-top: 22px;
  }
  .brand-mark {
    display: flex; align-items: center; gap: 10px;
    font-weight: 700; color: var(--brand-red); letter-spacing: 0.5px;
  }
  .brand-mark__dot {
    width: 14px; height: 14px; border-radius: 50%; background: var(--brand-orange);
  }
  .card--back .brand-mark { font-size: 30px; margin-bottom: 22px; }
  .contact-name {
    font-size: 17px; font-weight: 700; color: var(--ink);
    letter-spacing: 0.3px; margin-bottom: 8px;
  }
  .contact-lines { list-style: none; text-align: center; font-size: 13.5px; line-height: 1.4; color: var(--ink); }

  /* Front side: brand */
  .card--front { background: var(--brand-red); }
  .card--front .brand-band {
    position: absolute; left: 0; right: 0; top: 92px; height: 116px;
    background: var(--card-white);
    border-top: 5px solid var(--brand-orange);
    border-bottom: 5px solid var(--brand-orange);
    display: flex; align-items: center; justify-content: center;
  }
  .card--front .brand-plate {
    background: var(--brand-red);
    border: 5px solid var(--brand-orange);
    border-radius: 18px;
    padding: 26px 34px;
  }
  .card--front .brand-mark { font-size: 36px; color: var(--cream); }
</style>
</head>
<body>
<main class="card-sheet">
  <section class="card card--back" aria-label="Business card back">
    <div class="contact-panel">
      <div class="brand-mark"><span class="brand-mark__dot"></span><span>Breezeway Climate</span></div>
      <p class="contact-name">DOMINIC VASQUERELLI</p>
      <ul class="contact-lines">
        <li>Phone - 555-214-6837</li>
        <li>Email -dominic@breezeway.example</li>
        <li>www.BreezewayClimateLLC.example</li>
        <li>PO box 618 ,Millbrook NJ 07999</li>
      </ul>
    </div>
  </section>

  <section class="card card--front" aria-label="Business card front">
    <div class="brand-band">
      <div class="brand-plate">
        <div class="brand-mark"><span>Breezeway Climate</span></div>
      </div>
    </div>
  </section>
</main>
</body>
</html>
```